A new customer-driven VC fund for Enterprise IT Startups

I am bringing together a global group of customers (CIOs, CTOs, CISOs of Beacon 3000 companies) to help me identify and diligence best-of-breed Enterprise IT startups so I can invest in them via my new venture capital fund, Larkfen Ventures. In many ways, this is a new model for a VC fund and my goal is to revolutionize Venture Capital so that we hit the bull's eye in investing way more often in what is otherwise a guessing game for most VCs. So in the website, I'd like to capture the essences of global reach, best-of-breed, breakthrough innovation. I also want it to convey the ability of Larkfen Ventures to create category winners (i.e., if you want to be a market leader as a startup, you must take an investment from Larkfen Ventures).
My current website is www.larkfen-ventures.example - please use the content from the website within your design but please DO NOT use the design elements from the current website. INSTEAD, I'm looking for new and creative ideas on how I can leverage the existing content in a more appealing design -- any designs that look remotely similar to the existing website will be immediately declined.
I also want to ensure that the web design is mobile friendly.
Target Market(s)
Startup founders, potential investors, and other VCs
Industry/Entity Type
Venture Capital
Coding
Coded - Design and coding required
Number of Pages Required
1 page
Look and feel
Each slider illustrates characteristics of the customer's brand and the style your logo design should communicate.

```html
<!DOCTYPE html>
<html lang="en">
<head>
<meta charset="utf-8">
<title>Larkfen Ventures</title>
<link href="https://fonts.googleapis.com/css2?family=Fira+Sans:wght@400;600;700&family=Oswald:wght@500&family=Roboto+Condensed:wght@400;700&display=swap" rel="stylesheet">
<style>
:root{
  --navy:#142029;
  --navy-2:#1b2b36;
  --cyan:#6fe9f3;
  --cyan-soft:#c9f8fb;
  --teal:#2a6c8c;
  --teal-dark:#1f5a78;
  --ink:#1c2a33;
  --white:#ffffff;
}
*{box-sizing:border-box;margin:0;padding:0}
html,body{width:1200px;height:4722px;overflow:hidden}
body{font-family:"Fira Sans",sans-serif;color:var(--ink);background:var(--white);position:relative}
section,footer,header{position:absolute;left:0;width:1200px;overflow:hidden}
.abs{position:absolute}
.brand{font-family:"Fira Sans",sans-serif;font-weight:700;color:var(--white);font-size:30px;letter-spacing:.5px;display:flex;align-items:center;gap:10px}
.brand .dot{width:14px;height:14px;border-radius:50%;background:var(--cyan)}
.kicker{font-family:"Fira Sans",sans-serif;font-weight:700;color:var(--cyan);font-size:26px;letter-spacing:1px}
.sec-title{font-family:"Fira Sans",sans-serif;font-weight:700;font-size:32px;text-transform:uppercase}
.center{left:0;width:1200px;text-align:center}
.lead{font-family:"Roboto Condensed",sans-serif;font-size:16px;line-height:24px}

/* hero */
.hero{top:0;height:722px;background:linear-gradient(90deg,#101a21 0%,#17252f 55%,#223744 100%)}
.hero-visual{right:0;top:150px;width:560px;height:572px;background:radial-gradient(circle at 60% 55%,#5d6f7a 0%,#2b3c47 45%,rgba(23,37,47,0) 75%)}
.nav{top:40px;left:535px;display:flex;gap:24px;font-size:15px;color:var(--white);font-family:"Roboto Condensed",sans-serif}
.hero h1{font-weight:700}
.hero .l1{top:166px;left:174px;font-size:52px;color:var(--cyan)}
.hero .l2{top:230px;left:174px;font-size:44px;color:var(--white)}
.hero .l3{top:292px;left:174px;font-size:32px;color:var(--white);font-weight:600;font-family:"Roboto Condensed",sans-serif}
.hero p{top:350px;left:174px;width:440px;color:var(--white);font-size:17px;line-height:26px;text-align:justify;font-family:"Roboto Condensed",sans-serif}
.btn{top:436px;left:174px;width:143px;height:51px;border-radius:26px;background:var(--cyan);color:var(--navy);font-family:"Roboto Condensed",sans-serif;font-size:17px;display:flex;align-items:center;justify-content:center}
.dots{top:527px;left:174px;display:flex;gap:6px}
.dots i{width:12px;height:12px;border-radius:50%;background:#3e5563}
.dots i:first-child{background:var(--cyan)}

/* who */
.who{top:722px;height:725px;background:linear-gradient(160deg,#ffffff 0%,#eef5f8 60%,#e3eef3 100%)}
.card{width:260px;height:363px;border-radius:30px;overflow:hidden;background:linear-gradient(180deg,#d9fbfd,#aef3f8);box-shadow:0 8px 18px rgba(0,0,0,.12);text-align:center}
.card .photo{height:165px;background:linear-gradient(135deg,#8a9aa5,#cfd6db)}
.card h3{font-family:"Oswald",sans-serif;font-weight:500;font-size:17px;margin:26px 0 12px;text-transform:uppercase}
.card p{font-family:"Roboto Condensed",sans-serif;font-size:11.5px;line-height:17px;padding:0 20px}

/* focus */
.focus{top:1447px;height:660px;background:var(--navy)}
.area h4{font-weight:700;font-size:17px;color:var(--cyan);text-transform:uppercase;line-height:19px}
.area p{font-family:"Roboto Condensed",sans-serif;font-size:12px;color:var(--cyan);line-height:16px}
.area.left{text-align:right;width:230px}
.area.right{width:230px}

/* numbers */
.numbers{top:2107px;height:537px;background:linear-gradient(180deg,#2f7394,#2a6786)}
.numbers .kicker,.team .kicker{color:var(--white)}
.pill{top:284px;width:238px;height:137px;border:3px solid var(--cyan);border-radius:70px;background:rgba(255,255,255,.08);display:flex;align-items:center}
.pill .num{width:98px;height:125px;margin-left:3px;border-radius:62px 20px 20px 62px;background:var(--teal-dark);color:var(--white);font-weight:700;font-size:26px;display:flex;align-items:center;justify-content:center;text-align:center;line-height:28px}
.pill p{color:var(--white);font-family:"Roboto Condensed",sans-serif;font-size:12.5px;line-height:19px;padding:0 16px 0 12px}

/* themes */
.themes{top:2644px;height:732px;background:var(--white)}
.blob{left:161px;top:223px;width:477px;height:431px;border-radius:48% 52% 40% 60%/50% 40% 60% 50%;background:linear-gradient(135deg,#9fb0bb,#dfe6ea);box-shadow:-14px 8px 0 var(--cyan),10px 14px 0 var(--teal)}
.theme{left:676px;display:flex;align-items:center;gap:34px}
.theme .ico{width:80px;height:80px;border-radius:50%;background:var(--teal-dark);display:flex;align-items:center;justify-content:center}
.theme span{font-weight:600;font-size:21px;line-height:28px}

/* team */
.team{top:3376px;height:642px;background:linear-gradient(180deg,#2b6d8e,#25627f)}
.member{top:294px;width:183px;height:228px;border:3px solid var(--cyan);border-radius:28px;text-align:center;color:var(--cyan)}
.member .avatar{position:absolute;left:30px;top:-56px;width:118px;height:118px;border-radius:50%;border:5px solid var(--cyan);background:linear-gradient(135deg,#d6dde1,#8d9aa3)}
.member h5{margin-top:110px;font-family:"Oswald",sans-serif;font-weight:500;font-size:18px}
.member p{font-family:"Roboto Condensed",sans-serif;font-size:12.5px;line-height:17px;margin-top:6px;padding:0 8px}

/* engine */
.engine{top:4018px;height:612px;background:var(--white)}
.ecard{top:201px;width:260px;height:324px;border-radius:30px 30px 30px 70px;overflow:hidden;text-align:center;background:linear-gradient(180deg,#8cf0f7,#5fe0ec);box-shadow:0 8px 18px rgba(0,0,0,.15)}
.ecard.dark{background:linear-gradient(180deg,#3a7d9e,#24617f);color:var(--white)}
.ecard .corner{position:absolute;right:-20px;top:-30px;width:150px;height:150px;border-radius:50%;background:var(--teal-dark);display:flex;align-items:center;justify-content:center}
.ecard.dark .corner{background:var(--cyan)}
.ecard h3{position:absolute;top:150px;width:100%;font-family:"Oswald",sans-serif;font-weight:500;font-size:17px}
.ecard p{position:absolute;top:185px;width:100%;padding:0 24px;font-family:"Roboto Condensed",sans-serif;font-size:11.5px;line-height:17px}

footer{top:4630px;height:92px;background:#205e7c}
footer .copy{right:174px;top:38px;color:var(--white);font-family:"Roboto Condensed",sans-serif;font-size:13px}
</style>
</head>
<body>

<header class="hero">
  <div class="abs hero-visual" role="img" aria-label="Photo of an open hand holding a glowing rising bar and line chart"></div>
  <div class="abs brand" style="left:174px;top:28px">Larkfen Ventures</div>
  <nav class="abs nav"><span>HOME</span><span>ABOUT</span><span>NETWORK</span><span>TEAM &amp; ADVISORS</span><span>GTM ENGINE</span></nav>
  <h1 class="abs l1">WE INVEST IN</h1>
  <h1 class="abs l2">ENTERPRISE IT STARTUPS</h1>
  <h2 class="abs l3">at the Product-Market-Fit Stage</h2>
  <p class="abs">We are singularly focused on helping our portfolio companies gain a massive competitive advantage</p>
  <div class="abs btn">READ MORE</div>
  <div class="abs dots"><i></i><i></i><i></i></div>
</header>

<section class="who">
  <div class="abs center kicker" style="top:78px">LARKFEN</div>
  <h2 class="abs center sec-title" style="top:118px">Who We Are</h2>
  <p class="abs lead" style="left:230px;width:740px;top:180px;text-align:center">We only invest in post-product, post-revenue Enterprise IT startups. Usually, this means you're at Seed Extension to Series A stage.</p>
  <article class="abs card" style="left:172px;top:267px">
    <div class="photo" role="img" aria-label="Photo of business people shaking hands in an office"></div>
    <h3>Customers</h3>
    <p>Hundreds of the earliest-adopting CIOs, CTOs, and CISOs from Beacon 10 to Beacon 3000 to Cloud-First companies are a part of our exclusive network. An investment from Larkfen Ventures will give you immediate and exclusive access to hundreds of buyers around the world.</p>
  </article>
  <article class="abs card" style="left:469px;top:267px">
    <div class="photo" role="img" aria-label="Photo of colleagues reviewing documents at a desk"></div>
    <h3>Our Investment Philosophy</h3>
    <p>We only invest in startups that have broad &amp; immediate applicability across a global CIO base and are solving critical problems. To give our portfolio companies a truly unfair competitive advantage, we do not invest in competitive startups.</p>
  </article>
  <article class="abs card" style="left:768px;top:267px">
    <div class="photo" role="img" aria-label="Photo of a team discussing work around a laptop"></div>
    <h3>Customer-Led Investments</h3>
    <p>A global roster of CIOs leads our investment decision-making process. We also share candid, unfiltered feedback from dozens of customers via a Larkfen Memo™ with every single startup who presents to us - even if we don't end up investing.</p>
  </article>
</section>

<section class="focus">
  <div class="abs center kicker" style="top:73px">LARKFEN</div>
  <h2 class="abs center sec-title" style="top:112px;color:var(--white)">Investment Focus Areas</h2>
  <svg class="abs" style="left:0;top:0" width="1200" height="660" viewBox="0 0 1200 660">
    <defs><linearGradient id="hub" x1="0" y1="0" x2="0" y2="1"><stop offset="0" stop-color="#8ff3f8"/><stop offset="1" stop-color="#2f8fae"/></linearGradient></defs>
    <path d="M403 279 A205 205 0 1 0 797 279" fill="none" stroke="#c9d3d8" stroke-width="3"/>
    <circle cx="599" cy="358" r="152" fill="url(#hub)" stroke="#c9f8fb" stroke-width="4"/>
    <g fill="#2a6c8c" stroke="#ffffff" stroke-width="3">
      <circle cx="403" cy="279" r="30"/><circle cx="392" cy="378" r="30"/><circle cx="432" cy="475" r="30"/>
      <circle cx="797" cy="279" r="30"/><circle cx="802" cy="376" r="30"/><circle cx="766" cy="473" r="30"/>
    </g>
    <g fill="none" stroke="#ffffff" stroke-width="2">
      <path d="M403 266 l10 4 v8 c0 7 -5 11 -10 13 c-5 -2 -10 -6 -10 -13 v-8 z"/>
      <rect x="382" y="368" width="20" height="20" rx="4"/><circle cx="392" cy="378" r="4"/>
      <circle cx="432" cy="475" r="13"/><path d="M419 475 h26 M432 462 c-7 8 -7 18 0 26 c7 -8 7 -18 0 -26"/>
      <path d="M785 286 h24 a7 7 0 0 0 0 -14 a10 10 0 0 0 -19 2 a6 6 0 0 0 -5 12 z"/>
      <path d="M794 376 a6 6 0 1 1 8 0 a6 6 0 1 0 8 0" /><path d="M788 376 a6 6 0 1 0 12 0"/>
      <rect x="752" y="464" width="28" height="18" rx="9"/>
    </g>
  </svg>
  <div class="abs center" style="top:310px;left:460px;width:280px;text-align:center" >
    <span class="brand" style="justify-content:center;color:var(--navy);font-size:34px;line-height:44px;display:block">Larkfen<br>Ventures</span>
  </div>
  <div class="abs area left" style="left:129px;top:252px"><h4>Security</h4><p>Duis aute irure dolor in reprehen derit in voluptate</p></div>
  <div class="abs area left" style="left:120px;top:350px"><h4>AI &amp; ML</h4><p>Duis aute irure dolor in reprehen derit in voluptate</p></div>
  <div class="abs area left" style="left:158px;top:446px"><h4>Networking &amp;<br>Architecture</h4><p>Duis aute irure dolor in reprehen derit in voluptate</p></div>
  <div class="abs area right" style="left:840px;top:252px"><h4>Cloud &amp;<br>Infrastructure</h4><p>Duis aute irure dolor in reprehen derit in voluptate</p></div>
  <div class="abs area right" style="left:846px;top:350px"><h4>DevOps</h4><p>Duis aute irure dolor in reprehen derit in voluptate</p></div>
  <div class="abs area right" style="left:810px;top:446px"><h4>SaaS</h4><p>Duis aute irure dolor in reprehen derit in voluptate</p></div>
</section>

<section class="numbers">
  <div class="abs" style="inset:0;background:radial-gradient(circle at 55% 35%,rgba(120,170,195,.35),rgba(0,0,0,0) 55%)" role="img" aria-label="Faded photo of a businessman working on a laptop"></div>
  <div class="abs center kicker" style="top:80px">LARKFEN</div>
  <h2 class="abs center sec-title" style="top:118px;color:var(--white)">Strength in Numbers</h2>
  <p class="abs lead" style="left:330px;width:540px;top:180px;text-align:center;color:var(--white)">We collect and analyze monthly purchase intent data from a global network of IT decision-makers.</p>
  <div class="abs pill" style="left:97px"><div class="num">500+</div><p>Early adopting, influential CIOs, CTOs, CISOs and IT decision-makers</p></div>
  <div class="abs pill" style="left:352px"><div class="num">$<br>100B+</div><p>Annual enterprise technology purchasing budget across our network</p></div>
  <div class="abs pill" style="left:608px"><div class="num">15</div><p>Countries represented in our current network</p></div>
  <div class="abs pill" style="left:863px"><div class="num">550+</div><p>Purchase intent data points collected monthly</p></div>
</section>

<section class="themes">
  <div class="abs kicker" style="top:67px;left:383px;color:var(--teal)">LARKFEN</div>
  <h2 class="abs sec-title" style="top:104px;left:383px">Unifying Investment Themes</h2>
  <div class="abs blob" role="img" aria-label="Photo of a smiling bearded executive reading a tablet"></div>
  <div class="abs theme" style="top:278px"><div class="ico"><svg width="40" height="40" viewBox="0 0 40 40" fill="none" stroke="#fff" stroke-width="2.5"><circle cx="20" cy="20" r="16"/><path d="M4 20h32M20 4c-8 9-8 23 0 32c8-9 8-23 0-32"/></svg></div><span>Next-Gen Enterprise<br>IT Solutions</span></div>
  <div class="abs theme" style="top:397px"><div class="ico"><svg width="40" height="40" viewBox="0 0 40 40" fill="none" stroke="#fff" stroke-width="2.5"><path d="M20 4l5 11 12 1-9 8 3 12-11-6-11 6 3-12-9-8 12-1z"/></svg></div><span>Attacking Large Markets<br>With Universal Application</span></div>
  <div class="abs theme" style="top:518px"><div class="ico"><svg width="40" height="40" viewBox="0 0 40 40" fill="none" stroke="#fff" stroke-width="2.5"><path d="M20 6l16 8-16 8-16-8z M4 21l16 8 16-8 M4 28l16 8 16-8"/></svg></div><span>Products And Platforms<br>That Take A Holistic<br>Approach</span></div>
</section>

<section class="team">
  <div class="abs" style="inset:0;background:radial-gradient(circle at 50% 40%,rgba(110,160,185,.35),rgba(0,0,0,0) 60%)" role="img" aria-label="Faded photo of colleagues meeting"></div>
  <div class="abs center kicker" style="top:85px">LARKFEN</div>
  <h2 class="abs center sec-title" style="top:123px;color:var(--white)">Team, Investors &amp; Advisors</h2>
  <p class="abs lead" style="left:180px;width:840px;top:188px;text-align:center;color:var(--white)">We have built a world-class roster of executive advisors and mentors with exceptional go-to-market pedigrees to help our portfolio companies in their go-to-market journeys.</p>
  <div class="abs member" style="left:121px"><div class="avatar" role="img" aria-label="Portrait photo"></div><h5>Rafael M. Ostrand</h5><p>Founder &amp; Managing Director</p></div>
  <div class="abs member" style="left:313px"><div class="avatar" role="img" aria-label="Portrait photo"></div><h5>Hugo Pennant</h5><p>Founder &amp; Ex CEO, Corvane</p></div>
  <div class="abs member" style="left:507px"><div class="avatar" role="img" aria-label="Portrait photo"></div><h5>Devan Kapoor</h5><p>Co-founder, Stratalink (IPO), Queryloft</p></div>
  <div class="abs member" style="left:703px"><div class="avatar" role="img" aria-label="Portrait photo"></div><h5>Eli Marchetti</h5><p>Co-founder, Lakemoor ($2B+ valuation)</p></div>
  <div class="abs member" style="left:897px"><div class="avatar" role="img" aria-label="Portrait photo"></div><h5>Owen Brecht</h5><p>President, Silvergate Semis</p></div>
</section>

<section class="engine">
  <div class="abs kicker" style="top:67px;left:452px;color:var(--teal)">LARKFEN</div>
  <h2 class="abs sec-title" style="top:105px;left:452px">A Global GTM Engine</h2>
  <article class="abs ecard" style="left:172px">
    <div class="corner"><svg width="50" height="50" viewBox="0 0 50 50" fill="none" stroke="#fff" stroke-width="2.5"><rect x="18" y="8" width="24" height="32" rx="3"/><circle cx="15" cy="30" r="10"/><path d="M15 24v12M24 16h12M24 22h12"/></svg></div>
    <h3>GTM COACHES</h3>
    <p>We will partner with you to navigate the complex enterprise sales process by leveraging our executive network to provide product feedback, sales strategy, and market insights</p>
  </article>
  <article class="abs ecard dark" style="left:469px">
    <div class="corner"><svg width="60" height="40" viewBox="0 0 60 40" fill="none" stroke="#1f5a78" stroke-width="3"><path d="M4 14l12-6 14 8 14-8 12 6M10 18l16 14c2 2 5 2 7 0l17-14"/></svg></div>
    <h3>STRATEGIC PARTNERS</h3>
    <p>Strategic partnerships can propel a startup to the next level. Leverage our extensive network of IT Executives, Channel Partners, and OEMs to accelerate your path to becoming a category leader</p>
  </article>
  <article class="abs ecard" style="left:768px">
    <div class="corner"><svg width="50" height="50" viewBox="0 0 50 50" fill="none" stroke="#fff" stroke-width="2.5"><circle cx="25" cy="25" r="19"/><path d="M14 14c6 2 8 8 4 12s2 10 6 12M32 10c-2 6 4 8 8 10"/></svg></div>
    <h3>GLOBAL AMBASSADORS</h3>
    <p>Expanding globally is no simple exercise. Our network of Global IT Execs will provide on-the-ground intelligence, referrals, and influence as you conquer new geographies</p>
  </article>
</section>

<footer>
  <div class="abs brand" style="left:174px;top:28px">Larkfen Ventures</div>
  <p class="abs copy">Copyrights @ 2021 Larkfen Ventures. All Rights Reserved.</p>
</footer>

</body>
</html>
```